Q.R. Bright Desk Store

The design is for eCommerce home page but I would like it to complement this site: http://www.qrbrightdesksystems.com/ but... it should also have independence as a standalone site.

The best design will be able to effectively mix corporate with a high quality small business consumer feel. It should be completely custom design, not a template look or feel. I want the users to get the feeling that this is the place to go for buying tech for business. We sell the same products as Vantrel.

You can be creative as you wish, as long as the elements of a great eCommerce site are present.

I would like your 'design' to blow these away:
http://www.buying.zorvex.com/
mivoland.com
http://www.vantrel.com/

Here are references:
Call to action
http://trabelwise.com/us/blog/48173-seven-tips-for-designing-an-effective-ecommerce-call-to-action

Effective Ecommerce design
http://www.plov.com/ss/7-tips-for-effective-e-commerce#0

91 points of ecommerce
http://dreb.com/blog/holygrail-of-ecommerce-conversion-optimization-91-points-checklist

UPDATE 07/11/2013:

Please look at the category sample png files. I see already many people are using the main menu from qrbrightdesksystems.com and I do not mind your creativiety, but this is an eCommerce store and people need a menu to get to the categories and/or product types. I don't want to limit anyone creativity by the png samples. I'm also not using them to show I like them in any particular way or form, just that it's needed, whether it's a button (dropdown of course) that says 'Categories' or 'Products, whether it an accordion, horizontal or vertical.

Thanks

UPDATE 07/12/2013:

Please find other use of space that has been used for About Us paragraph (if you've added it to the page). About Us should have it's own page and the purpose of the design should be to sell products (and some services as products). Please put a link or some other creative method to lead users to the About Us page.

Reason: I've raised the award, including 1st, 2nd, and 3rd place and participation payments so I will also extend 7 days. Thanks!

I've updated the product brief. Please scroll down to where it says: UPDATE 07/11/2013

Thanks!

UPDATE 07/12/2013:

Please find other use of space that has been used for About Us paragraph (if you've added it to the page).  About Us should have it's own page and the purpose of the design should be to sell products (and some services as products). Please put a link or some other creative method to lead users to the About Us page if you must but not on the real estate of the page.

Thanks!

Added updates to the brief 7/14/2013.

Thanks!

The voting is in and the project is complete.  Thanks everyone for joining, all of those who participated are truly amazingly talented. But, there were only 3 prizes.  I will be having further projects down the line to develop other pages to this site after the initial implementation is completed.  I truly would like to have you all back. 

- Thank you.

Target Market(s)

corporate decision-makers AND small business consumers

Industry/Entity Type

Small Business

Requirements
Must have
• Call to action.
Openness (non-clutter).

These elements:
Search box
Logo
Tagline
Telephone number
Contact details
Address
My account / sign in
Shopping basket / checkout link
Latest offers
Promotional area
Email sign up
Delivery information
About us
Link to press office / corporate site
Terms and conditions
Sitemap for the footer.
Delivery offers: free
Personalized recommendations
Social media links
Accepted payment methods
Link to blog or community section
Change language / country

http://freshnotesblog.kelvarant.com/sales-leads-landing-page/

UPDATE 07/14/2013
Category Menu. This can be a dropdown, horizontal, vertical, etc. But shoppers need to know how to get to the products they want to buy.
Nice to have
• Trustmarks
Blog/Blog link

UPDATE 07/12/2013:
Make the footer useful.

UPDATE 07/14/2013 (Suggestions of elements to differentiate your designs)

-Quick Shop: A quick buy module/section: Where a user can put in a SKU number or Model number to quickly add the product to their shopping cart.

-Featured
-Best Sellers
-Specials
-Trending Tags/Tag Cloud
- Activity Stream
- Cross Sell/ Up Sell
- Testimonial
- Social Network Feed
- Live Help
- Feedback/Support/Contact Tab
- Show logged in user (i.e. Welcome, Mark Pell)
Should not have
• The design SHOULD NOT be generic like this:

http://www.artflock.com/design/52392
http://www.pelicanvault.com/

The page should not feel over cluttered. It should not have low quality icons or design elements. Navigation should not be hard to discover or confusing.

```html
<!DOCTYPE html>
<html lang="en">
<head>
<meta charset="utf-8">
<title>Q.R. Bright Desk Store</title>
<link href="https://fonts.googleapis.com/css2?family=Open+Sans:wght@400;600;700&family=Oswald:wght@400;600&display=swap" rel="stylesheet">
<style>
:root{
  --blue:#1a87cc;
  --blue-dark:#136aa3;
  --navy:#0e2a55;
  --navy-2:#0a2148;
  --red:#d0202a;
  --promo-red:#c3161c;
  --text:#444;
  --muted:#8a8a8a;
  --line:#e3e3e3;
  --soft:#f4f4f4;
  --white:#fff;
}
*{box-sizing:border-box;margin:0;padding:0}
html,body{width:1200px;height:3702px;overflow:hidden;background:var(--white);font-family:"Open Sans",Arial,sans-serif;color:var(--text);font-size:13px}
a{color:inherit;text-decoration:none}
ul{list-style:none}
.wrap{width:960px;margin:0 auto;position:relative}

/* top bar */
.topbar{height:30px}
.topbar .wrap{display:flex;justify-content:space-between;align-items:center;height:30px;font-size:11px}
.topbar .welcome a{color:var(--blue)}
.topbar .links{display:flex;gap:3px}
.topbar .links span{background:var(--navy);color:#fff;font-size:10px;font-weight:700;padding:4px 9px}

/* header */
.header{height:95px}
.header .wrap{display:flex;align-items:center;height:95px}
.logo{display:flex;align-items:center;gap:10px;width:430px}
.logo .mark{width:50px;height:50px;border-radius:50%;background:var(--navy)}
.logo .name{font-family:"Oswald",sans-serif;font-weight:600;font-size:30px;color:var(--navy);line-height:1}
.help,.cart{display:flex;gap:8px;align-items:center;width:170px;font-size:11px}
.help svg,.cart svg{flex:none}
.help b{display:block;color:var(--blue);font-size:12px}
.cart b{display:block;color:var(--blue)}
.cart .checkout{display:inline-block;background:var(--navy);color:#fff;font-size:10px;padding:1px 7px;border-radius:3px;margin-top:2px}
.search{margin-left:auto;display:flex;align-items:center;border:1px solid #ccc;width:190px;height:30px;padding:0 8px;font-size:11px;color:var(--muted);justify-content:space-between}

/* nav */
.nav{height:55px}
.nav ul{display:flex;border-bottom:1px solid var(--line);height:42px;margin-top:5px}
.nav li{flex:1;text-align:center;line-height:42px;font-size:14px;border:1px solid var(--line);border-bottom:0;background:var(--soft);color:#555}
.nav li.active{background:#fff;font-weight:600;color:var(--navy)}

/* hero */
.hero{height:585px;padding-top:15px}
.hero .wrap{display:flex;gap:12px}
.sidebar{width:250px;height:565px;border:1px solid var(--line)}
.sidebar h3{background:var(--navy);color:#fff;padding:12px 16px;font-size:13px;font-weight:600;line-height:1.1}
.sidebar h3 span{display:block;font-family:"Oswald",sans-serif;font-size:26px;font-weight:400}
.sidebar li{font-size:11px;font-weight:600;padding:7px 16px;border-bottom:1px solid var(--line);color:#333}
.sidebar li.sub{font-weight:400;font-size:10px;color:#666;padding-left:26px}
.sidebar li::before{content:"▸ ";color:var(--blue)}
.hero-main{flex:1}
.slider{height:440px;position:relative;background:linear-gradient(120deg,#c8d4df,#eef2f5 55%,#9fb0c0);display:flex}
.slider .photo{width:420px;height:100%;background:linear-gradient(160deg,#b9c6d2,#dfe6ec 60%,#8e9eae)}
.slider .copy{margin-left:auto;padding:30px 30px 0 0;text-align:right}
.slider .copy h2{font-family:"Oswald",sans-serif;font-size:50px;line-height:1;color:var(--navy);font-weight:600}
.slider .copy h2 span{color:var(--blue);font-weight:400;display:block}
.slider .copy p{font-size:14px;color:var(--navy)}
.dots{position:absolute;left:20px;bottom:14px;display:flex;gap:6px}
.dots i{width:8px;height:8px;border-radius:50%;background:#fff;opacity:.6}
.dots i:first-child{opacity:1}
.offers{height:110px;margin-top:15px;background:var(--navy);display:flex;align-items:center;padding:0 28px;color:#fff;justify-content:space-between}
.offers .latest{font-family:"Oswald",sans-serif;font-size:34px;line-height:.95;background:var(--blue);padding:8px 18px;border-radius:6px}
.offers .racks{width:200px;height:80px;background:linear-gradient(180deg,#8c96a3,#4a5563)}
.offers .disc{font-family:"Oswald",sans-serif;font-size:58px;line-height:.9;text-align:right}
.offers .disc small{display:block;font-size:26px}

/* products */
.products{height:1196px;padding-top:20px}
.products .wrap{display:flex;border-top:1px solid var(--line)}
.col{width:480px;border-right:1px solid var(--line)}
.col:last-child{border-right:0;border-left:1px solid var(--line)}
.item{border-bottom:1px solid var(--line);padding:22px 20px;position:relative}
.item .pic{background:linear-gradient(150deg,#cfd3d8,#6d7480);border-radius:2px}
.item h4{font-family:"Oswald",sans-serif;color:var(--blue);font-size:21px;font-weight:400;letter-spacing:.5px;margin:6px 0 4px}
.item p{font-size:10.5px;color:var(--muted);line-height:1.45}
.item .price{color:var(--red);font-family:"Oswald",sans-serif;font-size:28px;margin-top:8px;display:flex;align-items:center;justify-content:space-between}
.btn-shop{font-family:"Open Sans",sans-serif;font-size:10px;color:#555;border:1px solid #ccc;border-radius:12px;padding:3px 10px}
.row{display:flex;border-bottom:1px solid var(--line)}
.row .item{border-bottom:0;flex:1}
.row .item+.item{border-left:1px solid var(--line)}
.side-by-side{display:flex;gap:18px}
.side-by-side .pic{flex:none}

/* best sellers / promo */
.duo{display:flex;border-bottom:1px solid var(--line)}
.duo>div{width:480px;padding:22px 20px}
.duo>div+div{border-left:1px solid var(--line)}
.sec-title{font-family:"Oswald",sans-serif;color:var(--blue);line-height:1}
.sec-title small{display:block;font-size:15px;font-weight:400}
.sec-title span{font-size:36px;font-weight:400}
.best{height:515px}
.best-head{display:flex;justify-content:space-between;align-items:flex-end}
.arrows{display:flex;gap:4px}
.arrows i{width:30px;height:30px;border:1px solid #ccc;display:flex;align-items:center;justify-content:center}
.best-items{display:flex;gap:22px;margin-top:22px}
.best-items .item{padding:0;border:0;width:200px}
.promo{background:var(--promo-red);height:230px;margin-top:18px;color:#fff;padding:22px 30px;font-family:"Oswald",sans-serif}
.promo .t{font-size:22px}
.promo .save{font-size:74px;line-height:1;display:flex;align-items:flex-start;gap:10px}
.promo .save sup{font-size:22px}
.promo .n{font-family:"Open Sans",sans-serif;font-size:11px;text-align:center}
.body-copy{font-size:10.5px;color:var(--muted);line-height:1.55;margin-top:14px}

.feed-row{height:350px}
.quote{font-size:10.5px;color:var(--muted);line-height:1.6;margin-top:16px}
.quote b{display:block;color:var(--red);margin-top:10px;font-weight:400}
.feed li{display:flex;gap:12px;padding:12px 0;border-bottom:1px solid var(--line);font-size:10.5px;color:#666}
.feed li i{flex:none;width:26px;height:26px;background:var(--navy)}
.feed li em{color:var(--blue);font-style:normal}

.signup{height:175px}
.field{display:flex;margin-top:14px}
.field span{flex:1;border:1px solid #ccc;height:32px;font-size:11px;color:var(--muted);padding:8px}
.field b{background:var(--blue);color:#fff;font-weight:600;padding:0 14px;line-height:32px;font-size:12px}

/* delivery */
.delivery{height:115px;padding-top:10px}
.delivery .wrap{display:flex;height:95px;border-top:1px solid var(--line);border-bottom:1px solid var(--line)}
.delivery .cell{flex:1;display:flex;gap:12px;align-items:center;padding:0 20px}
.delivery .cell.live{background:var(--blue);color:#fff}
.delivery h5{font-family:"Oswald",sans-serif;color:var(--blue);font-size:18px;font-weight:400}
.delivery .live h5{color:#fff}
.delivery p{font-size:10px;color:var(--muted)}
.delivery .live p{color:#dbeefa}
.pay{display:flex;gap:5px;margin-top:6px}
.pay i{width:36px;height:22px;background:#c9ced6;border-radius:2px}
.pay i:nth-child(2){background:#2d4f9c}
.pay i:nth-child(3){background:#d98c2a}

/* footer */
.footer .wrap{background:var(--navy);height:510px;display:grid;grid-template-columns:repeat(4,1fr);padding:28px 30px;color:#c6d3e6;font-size:10.5px;gap:0 24px}
.footer h6{color:#fff;font-size:12px;font-weight:700;margin:0 0 6px}
.footer li{line-height:1.6}
.footer .grp{margin-bottom:16px}
.contact li{display:flex;gap:6px;align-items:flex-start}
.social{display:flex;gap:5px}
.social i{width:22px;height:22px;background:#2c5a98}
.copyright{height:22px}
.copyright .wrap{background:var(--navy-2);color:#9fb1cc;font-size:10px;text-align:center;line-height:22px}
</style>
</head>
<body>

<div class="topbar"><div class="wrap">
  <div class="welcome">Welcome visitor you can <a href="#">Login</a> or <a href="#">Create an Account</a> | <a href="#">My Account</a></div>
  <div class="links"><span>HOME</span><span>SMALL BUSINESS</span><span>ENTERPRISE</span><span>NON PROFIT</span><span>LANGUAGE ▾</span><span>COUNTRY ▾</span></div>
</div></div>

<header class="header"><div class="wrap">
  <a class="logo" href="#"><span class="mark"></span><span class="name">QR BRIGHT DESK</span></a>
  <div class="help">
    <svg width="26" height="26" viewBox="0 0 24 24"><path fill="#1a87cc" d="M6.6 10.8a15 15 0 006.6 6.6l2.2-2.2a1 1 0 011-.25 11 11 0 003.6.6 1 1 0 011 1V20a1 1 0 01-1 1A17 17 0 013 4a1 1 0 011-1h3.5a1 1 0 011 1 11 11 0 00.6 3.6 1 1 0 01-.25 1z"/></svg>
    <div>We're Here to Help US.<b>1 (888) XXX XXXX</b></div>
  </div>
  <div class="cart">
    <svg width="28" height="26" viewBox="0 0 24 22"><path fill="#1a87cc" d="M1 1h4l2.7 12.4a2 2 0 002 1.6h9.7a2 2 0 002-1.6L23 5H6"/><circle cx="9" cy="19" r="2" fill="#1a87cc"/><circle cx="19" cy="19" r="2" fill="#1a87cc"/></svg>
    <div><b>Shopping Cart</b>(0) Items<br><span class="checkout">Checkout</span></div>
  </div>
  <div class="search">Enter your Keywords... <svg width="12" height="12" viewBox="0 0 12 12"><circle cx="5" cy="5" r="4" fill="none" stroke="#666" stroke-width="1.5"/><path d="M8 8l3 3" stroke="#666" stroke-width="1.5"/></svg></div>
</div></header>

<nav class="nav"><div class="wrap"><ul>
  <li class="active">Hardware Fulfillment</li><li>Software Licensing</li><li>IT Resource Management</li><li>Technology Services</li>
</ul></div></nav>

<section class="hero"><div class="wrap">
  <aside class="sidebar">
    <h3>PRODUCT<span>CATEGORIES</span></h3>
    <ul>
      <li class="sub">MANUFACTURERS</li><li class="sub">A/Z DIRECTORY</li><li class="sub">AUTHORIZATIONS</li><li class="sub">NEW MANUFACTURERS</li><li class="sub">STORES</li>
      <li>TECHNOLOGY SOLUTIONS</li><li>COMMUNITIES</li><li>BUSINESS SUPPORT</li><li>SALES SUPPORT</li><li>TECHNICAL SUPPORT</li><li>FINANCIAL SUPPORT</li><li>CUSTOMER SERVICE</li><li>TRAINING AND EVENTS</li><li>DIVISIONS</li>
    </ul>
  </aside>
  <div class="hero-main">
    <div class="slider">
      <div class="photo" role="img" aria-label="Person working on a laptop seated among cloud-like server racks"></div>
      <div class="copy"><h2>CLOUD<span>SERVICES</span></h2><p>Where Disaster Don't Strike</p></div>
      <div class="dots"><i></i><i></i><i></i></div>
    </div>
    <div class="offers">
      <div class="latest">Latest<br>Offers</div>
      <div class="racks" role="img" aria-label="Row of rack-mounted servers"></div>
      <div class="disc">30%<small>DISCOUNT</small></div>
    </div>
  </div>
</div></section>

<section class="products"><div class="wrap">
  <div class="col">
    <div class="item" style="height:292px">
      <div class="side-by-side">
        <div class="pic" style="width:180px;height:150px" role="img" aria-label="Office laser printer"></div>
        <div><h4>PRINTERS</h4><p>Short product summary for business printers with quick specs, warranty info and support options included here.</p>
        <div class="price">$520 <span class="btn-shop">SHOP NOW ▸</span></div></div>
      </div>
    </div>
    <div class="row" style="height:442px">
      <div class="item"><div class="pic" style="width:110px;height:160px;margin:0 auto 16px;background:linear-gradient(150deg,#444,#111)" role="img" aria-label="Tablet device"></div>
        <h4>TABLETS</h4><p>Short product summary for business tablets with quick specs and support options included.</p>
        <div class="price">$520 <span class="btn-shop">SHOP NOW ▸</span></div></div>
      <div class="item"><div class="pic" style="width:130px;height:160px;margin:0 auto 16px" role="img" aria-label="Desk IP telephone"></div>
        <h4>TELECOM</h4><p>Short product summary for office phones with quick specs and support options included.</p>
        <div class="price">$520 <span class="btn-shop">SHOP NOW ▸</span></div></div>
    </div>
    <div class="item" style="height:442px;border-bottom:0">
      <div class="pic" style="width:400px;height:230px;margin:0 auto 18px" role="img" aria-label="Business projector with remote"></div>
      <h4>PROJECTORS</h4><p>Short product summary for meeting room projectors with brightness ratings, lamp life details, quick specs and support options included here.</p>
      <div class="price">$520 <span class="btn-shop">SHOP NOW ▸</span></div>
    </div>
  </div>
  <div class="col">
    <div class="item" style="height:482px">
      <div class="pic" style="width:260px;height:250px;margin:10px auto 26px;background:linear-gradient(150deg,#1b3d8f,#0b1c4a)" role="img" aria-label="Widescreen monitor"></div>
      <h4>MONITERS</h4><p>Short product summary for business monitors with screen sizes, panel types, quick specs and support options included here for buyers.</p>
      <div class="price">$520 <span class="btn-shop">SHOP NOW ▸</span></div>
    </div>
    <div class="item" style="height:504px">
      <div class="pic" style="width:240px;height:260px;margin:0 auto 20px;background:linear-gradient(150deg,#3a3f47,#0e1014)" role="img" aria-label="Rack server cabinets"></div>
      <h4>SERVERS</h4><p>Short product summary for rack and tower servers with quick specs, service plans and support options included here.</p>
      <div class="price">$520 <span class="btn-shop">SHOP NOW ▸</span></div>
    </div>
    <div class="item" style="height:190px;border-bottom:0">
      <div class="side-by-side">
        <div class="pic" style="width:150px;height:110px;background:linear-gradient(150deg,#2c5d9a,#0f223d)" role="img" aria-label="Computer motherboard"></div>
        <div><h4>ACCESSORIES</h4><p>Short summary for cables, boards and add-ons with quick specs included.</p>
        <div class="price">$520 <span class="btn-shop">SHOP NOW ▸</span></div></div>
      </div>
    </div>
  </div>
</div></section>

<div class="wrap">
  <div class="duo best" style="border-top:1px solid var(--line)">
    <div>
      <div class="best-head"><div class="sec-title"><small>BEST</small><span>SELLERS</span></div>
        <div class="arrows"><i><svg width="8" height="12" viewBox="0 0 8 12"><path d="M7 1L2 6l5 5" fill="none" stroke="#555" stroke-width="2"/></svg></i><i><svg width="8" height="12" viewBox="0 0 8 12"><path d="M1 1l5 5-5 5" fill="none" stroke="#555" stroke-width="2"/></svg></i></div></div>
      <div class="best-items">
        <div class="item"><div class="pic" style="width:110px;height:160px;margin:10px auto 20px;background:linear-gradient(150deg,#444,#111)" role="img" aria-label="Best selling tablet"></div>
          <h4>BEST 1</h4><p>Short product summary for a top selling item with quick specs and support options.</p>
          <div class="price">$96 <span class="btn-shop">SHOP NOW ▸</span></div></div>
        <div class="item"><div class="pic" style="width:110px;height:160px;margin:10px auto 20px;background:linear-gradient(150deg,#444,#111)" role="img" aria-label="Best selling tablet"></div>
          <h4>BEST 2</h4><p>Short product summary for a top selling item with quick specs and support options.</p>
          <div class="price">$95 <span class="btn-shop">SHOP NOW ▸</span></div></div>
      </div>
    </div>
    <div>
      <div class="sec-title"><small>ABOUT</small><span>COMPANY</span></div>
      <p class="body-copy">We supply business technology to companies of every size, from single offices to large enterprises. Our team sources hardware, software licensing and services from trusted vendors, and backs every order with fast delivery and friendly support. Learn more about our history, our partners and the people behind the store on our about page.</p>
      <div class="promo">
        <div class="t">START YOUR SHOPPING EARLY AND...</div>
        <div class="save"><span style="font-size:40px;line-height:1">SAVE<br>UP TO</span>50<sup>%<br>OFF</sup></div>
        <div class="n">This Offer is valid on all our store items!</div>
      </div>
    </div>
  </div>

  <div class="duo feed-row">
    <div>
      <div class="sec-title"><small>CLIENT'S</small><span>SPEAK</span></div>
      <p class="quote">" Ordering was simple and the team guided us through every step. Our new servers arrived on time, were configured as promised and the support staff answered every question quickly. We now buy all of our office technology here and recommend the store to other business owners without hesitation. "<b>- Client's Name</b></p>
    </div>
    <div>
      <div class="sec-title"><small>SOCIAL</small><span>FEED</span></div>
      <ul class="feed">
        <li><i></i><div>New arrivals in the server range are live today, see the full list online. <em>48 days ago</em></div></li>
        <li><i></i><div>Join us for a free webinar on cloud backup for small offices. <em>Posted To wall</em> · 4 days ago</div></li>
        <li><i></i><div>Thanks to everyone who shared our spring offers this week. <em>Shared</em> · 2 days ago</div></li>
      </ul>
    </div>
  </div>

  <div class="duo signup">
    <div>
      <div class="sec-title"><small>SUBSCRIBE</small><span>OUR NEWSLETTER</span></div>
      <p class="body-copy" style="margin-top:8px">Enter your email address below to receive occasional offers, discounts and promotions.</p>
      <div class="field"><span>Enter your email address...</span><b>SUBSCRIBE</b></div>
    </div>
    <div>
      <div class="sec-title"><small>SEARCH PRODUCT BY</small><span>SKU NUMBER</span></div>
      <p class="body-copy" style="margin-top:8px">Enter your SKU number or Model number to quickly add the product to their shopping cart.</p>
      <div class="field"><span>Enter your SKU Number</span><b>GO</b></div>
    </div>
  </div>
</div>

<section class="delivery"><div class="wrap">
  <div class="cell">
    <svg width="40" height="28" viewBox="0 0 40 28"><path fill="#1a87cc" d="M0 2h24v18H0zM26 8h8l6 7v5H26z"/><circle cx="8" cy="23" r="4" fill="#1a87cc" stroke="#fff" stroke-width="2"/><circle cx="32" cy="23" r="4" fill="#1a87cc" stroke="#fff" stroke-width="2"/></svg>
    <div><h5>FREE DELIVERY</h5><p>On All orders over $25 &amp; shipping!</p></div>
  </div>
  <div class="cell live">
    <svg width="34" height="34" viewBox="0 0 34 34"><circle cx="17" cy="11" r="7" fill="#fff"/><path d="M3 33a14 14 0 0128 0z" fill="#fff"/></svg>
    <div><h5>LIVE HELP</h5><p>Email and Live Chat support is available to help you in all your questions.</p></div>
  </div>
  <div class="cell"><div><h5>PAYMENT METHOD</h5><div class="pay"><i></i><i></i><i></i><i></i><i></i></div></div></div>
</div></section>

<footer class="footer"><div class="wrap">
  <div>
    <div class="grp"><h6>Hardware Fulfillment</h6><ul><li>Products</li><li>Benefits</li><li>Services</li><li>Why Us?</li></ul></div>
    <div class="grp"><h6>Software Licensing</h6><ul><li>Norvane</li><li>Quillex</li><li>Barrowtek</li><li>Larkspur</li><li>Orbelle</li><li>Zorvex</li><li>Tandrel</li><li>Kesmo</li><li>Crimson Loft</li><li>Veltacom</li><li>Hollisoft</li><li>Dravia</li><li>Ostrel</li><li>Shieldwin</li></ul></div>
  </div>
  <div>
    <div class="grp"><h6>IT Resource Management</h6><ul><li>Employees</li><li>Candidates</li><li>Outsourcing</li><li>Insights</li></ul></div>
    <div class="grp"><h6>Technology Services</h6><ul><li>Managed Services</li><li>Hardware Maintenance</li><li>Data Backup &amp; Recovery</li><li>Communication Services</li><li>Email Hosting and Websites</li><li>IT Service Management</li><li>Project Management</li><li>Advisory Consulting</li><li>Vendor Management</li><li>Business Intelligence</li></ul></div>
    <div class="grp"><h6>Programs</h6><ul><li>Exchange Board</li><li>Partner Program</li><li>Recycle</li></ul></div>
  </div>
  <div>
    <div class="grp"><h6>Main Menu</h6><ul><li>Home</li><li>Small Business</li><li>Enterprise</li><li>Non-Profit</li></ul></div>
    <div class="grp"><h6>User Menu</h6><ul><li>Go Shopping</li><li>Billing</li><li>Blog</li><li>Community</li><li>Press Office</li><li>Corporate Office</li><li>Get Support</li><li>Contact Us</li></ul></div>
    <div class="grp"><h6>Our Website</h6><ul><li>qrbrightdeskstore.com</li><li>qrbrightdeskinc.com</li><li>qrbrightdesksystems.com</li><li>qrbrightdeskeducation.com</li></ul></div>
  </div>
  <div>
    <div class="grp"><h6>Our Company</h6><ul><li>About Us</li><li>Careers</li><li>Corporate</li><li>Partners</li></ul></div>
    <div class="grp"><h6>Other Links</h6><ul><li>Press Office</li><li>Corporate Office</li><li>Terms &amp; Conditions</li></ul></div>
    <div class="grp contact"><h6>Contact Details</h6><ul>
      <li><svg width="10" height="14" viewBox="0 0 10 14"><path fill="#c6d3e6" d="M5 0a5 5 0 015 5c0 4-5 9-5 9S0 9 0 5a5 5 0 015-5z"/></svg>42 Linden Court, Suite #118<br>Maplewood, NY 10580</li>
      <li><svg width="10" height="12" viewBox="0 0 24 24"><path fill="#c6d3e6" d="M6.6 10.8a15 15 0 006.6 6.6l2.2-2.2 4.6 1.6V21A17 17 0 013 4h5l1 4.6z"/></svg>+1 (888) XXX XXXX<br>+1 (888) XXX XXXX</li>
      <li><svg width="12" height="10" viewBox="0 0 12 10"><rect width="12" height="10" fill="#c6d3e6"/><path d="M0 0l6 5 6-5" fill="none" stroke="#0e2a55"/></svg>info@qrbrightdesksystems.com</li>
    </ul></div>
    <div class="grp"><h6>Follow Us</h6><div class="social"><i></i><i></i><i></i><i></i><i></i><i></i></div></div>
  </div>
</div></footer>

<div class="copyright"><div class="wrap">Copyright © 2013 Q.R. Bright Desk Store. All Rights Reserved.</div></div>

</body>
</html>
```